Animal Eye Clinic needs a Business card

We are a new veterinary ophthalmology practice (Tessaly Animal Eye Care) and we need a business card designed. We only see animal eyes - we are not a regular veterinary clinic. We already have a logo. We are looking for a professional, good looking business card to hand out to our clients. We are looking for something simple but professional and contemporary. Our logo is likely the only picture/graphic that needs to be on the card.
Updates

Contact Information for Business Card

Marisol Dunkley, BSc, DVM, MSc, DipACVO
Veterinary Ophthalmologist

Phone: 250.418.3097
Email: tessalyanimaleyecare@mailbrook.net
Website: tessalyanimaleyecare.net
Address: 1840 Pellworth Rd
Kelowna, BC, V4T 8M3

Colors

Designer to choose colors to be used in the design.

Requirements
Must have
• Our logo (attached)

```html
<!DOCTYPE html>
<html lang="en">
<head>
<meta charset="utf-8">
<title>Tessaly Animal Eye Care — Business Card</title>
<link rel="stylesheet" href="https://fonts.googleapis.com/css2?family=Roboto:wght@400;500&display=swap">
<style>
  :root {
    --backdrop: #1b1b1b;
    --card: #2a2a2a;
    --teal: #1597a8;
    --silver: #b9b9b9;
    --text: #e9e9e9;
  }
  html, body {
    margin: 0;
    padding: 0;
    width: 1200px;
    height: 900px;
    overflow: hidden;
    background: var(--backdrop);
    font-family: "Roboto", Arial, sans-serif;
  }
  .stage {
    width: 1200px;
    height: 900px;
    display: flex;
    flex-direction: column;
    align-items: center;
    justify-content: center;
    gap: 40px;
  }
  .card {
    position: relative;
    width: 630px;
    height: 360px;
    background: var(--card);
    box-shadow: 0 14px 30px rgba(0,0,0,.55);
    overflow: hidden;
  }
  .card::after {
    content: "";
    position: absolute;
    left: 0; right: 0; bottom: 0;
    height: 8px;
    background: var(--teal);
  }

  /* Front */
  .card-front {
    display: flex;
    align-items: center;
    justify-content: center;
    gap: 18px;
  }
  .brand-dot {
    width: 58px;
    height: 58px;
    border-radius: 50%;
    background: #3a3a3a;
  }
  .brand-name {
    color: var(--silver);
    font-weight: 500;
    font-size: 30px;
    letter-spacing: 1px;
    text-transform: uppercase;
    margin: 0;
  }

  /* Back */
  .card-back {
    display: flex;
    align-items: center;
  }
  .brand-block {
    width: 230px;
    display: flex;
    flex-direction: column;
    align-items: center;
    gap: 14px;
    padding-left: 30px;
  }
  .brand-block .brand-dot {
    width: 130px;
    height: 130px;
    background: var(--teal);
  }
  .brand-block .brand-name {
    color: var(--teal);
    font-size: 16px;
    text-align: center;
  }
  .contact {
    padding-left: 40px;
    color: var(--text);
  }
  .person-name {
    margin: 0;
    color: var(--teal);
    font-weight: 500;
    font-size: 34px;
  }
  .credentials, .role {
    margin: 2px 0 0;
    font-size: 16px;
    color: #d6d6d6;
  }
  .address {
    margin: 16px 0 14px;
    font-size: 18px;
    line-height: 1.3;
    font-style: normal;
  }
  .contact-list {
    list-style: none;
    margin: 0;
    padding: 0;
    font-size: 17px;
  }
  .contact-list li {
    display: flex;
    align-items: center;
    gap: 10px;
    margin-bottom: 4px;
  }
  .contact-list svg {
    width: 14px;
    height: 14px;
    flex: none;
  }
</style>
</head>
<body>
<main class="stage">
  <section class="card card-front">
    <span class="brand-dot"></span>
    <p class="brand-name">Tessaly Animal Eye Care</p>
  </section>

  <section class="card card-back">
    <div class="brand-block">
      <span class="brand-dot"></span>
      <p class="brand-name">Tessaly Animal Eye Care</p>
    </div>
    <div class="contact">
      <h1 class="person-name">Marisol Dunkley</h1>
      <p class="credentials">BSc, DVM, MSc, DipACVO</p>
      <p class="role">Veterinary Ophthalmologist</p>
      <address class="address">Address: 1840 Pellworth Rd<br>Kelowna, BC, V4T 8M3</address>
      <ul class="contact-list">
        <li>
          <svg viewBox="0 0 16 16" aria-hidden="true"><path d="M4 1 L6.5 4 L5 6 Q6.5 9.5 10 11 L12 9.5 L15 12 L13 15 Q4 14 1 3 Z" fill="var(--teal)"/></svg>
          250.418.3097
        </li>
        <li>
          <svg viewBox="0 0 16 16" aria-hidden="true"><rect x="1" y="3" width="14" height="10" fill="none" stroke="var(--teal)" stroke-width="1.5"/><path d="M1 3 L8 9 L15 3" fill="none" stroke="var(--teal)" stroke-width="1.5"/></svg>
          tessalyanimaleyecare@mailbrook.net
        </li>
        <li>
          <svg viewBox="0 0 16 16" aria-hidden="true"><circle cx="8" cy="8" r="6.5" fill="none" stroke="var(--teal)" stroke-width="1.4"/><ellipse cx="8" cy="8" rx="3" ry="6.5" fill="none" stroke="var(--teal)" stroke-width="1.2"/><path d="M1.5 8 H14.5" stroke="var(--teal)" stroke-width="1.2"/></svg>
          www.tessalyanimaleyecare.net
        </li>
      </ul>
    </div>
  </section>
</main>
</body>
</html>
```